Redesign of an educational Eye website for Medical Students and Healthcare professionals

www.corvellelearninghub.com is an educational resource, illustrated using high quality 3D animations, for undergraduate medical students and healthcare professionals to learn about the anatomy of the human eye and associated common eye disorders.

The website was originally developed (using a Joomla template) a couple of years ago and we now want to update the brand and design of the site. Example content and animations can be found at https://www.corvellelearninghub.com/overview or https://www.corvellelearninghub.com/ocular-anatomy/orbital-anatomy

We would like a new logo and home page design (to include new colour palette, fonts and updated overall design).

The attached PowerPoint contains an example layout of the revised components we want to appear on the new Home page. We plan to have a hero panel at the top of page playing a short video of some of the animations. Similar to how this site works (www.zeptal.uk.com).

We want the new site to feel Professional, Modern and Clean and simple.

Target Market(s)

Undergraduate medical students and Healthcare Professionals

Industry/Entity Type

Medical

Logo Text

Corvelle Learning Hub

Number of Pages Required

1 page

Font styles to use
Sans Serif

Colors

Designer to choose colors to be used in the design.

```html
<!DOCTYPE html>
<html lang="en">
<head>
<meta charset="utf-8">
<title>Corvelle Learning Hub</title>
<link href="https://fonts.googleapis.com/css2?family=Raleway:wght@300;400;500;600;700&display=swap" rel="stylesheet">
<style>
:root{
  --brand:#3c4a9e;
  --brand-light:#5a6fcf;
  --ink:#1d1f2b;
  --muted:#7a7f8e;
  --pale:#e9eef5;
  --line:#d6dbe6;
  --white:#ffffff;
}
*{box-sizing:border-box;margin:0;padding:0}
html,body{width:1200px;height:4688px;overflow:hidden}
body{font-family:'Raleway',Arial,sans-serif;color:var(--ink);background:var(--white);position:relative}
section,header,footer{position:relative;width:1200px;overflow:hidden}
.accent{color:var(--brand-light)}
.section-title{font-weight:300;font-size:38px;text-align:center;color:var(--ink);position:relative;z-index:2}
.btn{display:inline-block;font-size:15px;padding:12px 26px;text-decoration:none}
.btn-dark{background:#111;color:var(--white)}
.btn-brand{background:var(--brand);color:var(--white)}
.btn-outline{border:1px solid var(--brand);color:var(--brand);background:var(--white);font-size:13px;padding:10px 24px}

/* header */
.site-header{height:125px;display:flex;align-items:center;justify-content:space-between;padding:0 80px;background:var(--white);box-shadow:0 2px 10px rgba(0,0,0,.05);z-index:3}
.brand{display:flex;align-items:center;gap:12px;text-decoration:none}
.brand-mark{width:22px;height:22px;border-radius:50%;background:var(--brand-light)}
.brand-name{font-size:30px;font-weight:400;color:var(--brand);line-height:1}
.brand-sub{display:block;font-size:14px;letter-spacing:3px;color:var(--brand);margin-top:4px}
.main-nav{display:flex;align-items:center;gap:44px;font-size:14px;letter-spacing:1px}
.main-nav a{color:#9aa0b0;text-decoration:none}
.main-nav a.active{color:var(--brand)}
.main-nav .login{background:var(--brand);color:var(--white);padding:12px 22px}

/* hero */
.hero{height:547px}
.hero-media{position:absolute;inset:0;
  background:
    linear-gradient(90deg,rgba(236,242,247,.96) 0%,rgba(228,237,244,.85) 38%,rgba(228,237,244,0) 62%),
    linear-gradient(180deg,#bcd0e0 0%,#9fb9cf 45%,#d9c3b4 100%),
    #c4d5e3}
.hero-tone{position:absolute;left:620px;top:0;width:580px;height:547px;
  background:linear-gradient(100deg,rgba(176,200,220,0) 0%,#a8c0d6 20%,#dcc6b8 55%,#e9d8cc 80%,#f2e6dd 100%);
  -webkit-mask-image:linear-gradient(90deg,transparent,#000 25%);mask-image:linear-gradient(90deg,transparent,#000 25%)}
.hero-copy{position:absolute;left:80px;top:292px;width:560px;z-index:2}
.hero-copy h1{font-size:43px;font-weight:700;color:#111;margin-bottom:14px}
.hero-copy p{font-size:14.5px;line-height:1.45;color:#222;margin-bottom:26px}
.hero-copy .btn{margin-right:10px;font-size:14px;padding:12px 22px}

/* partners */
.partners{height:266px;padding-top:58px}
.partners .section-title{font-size:36px}
.partner-row{display:flex;justify-content:space-between;align-items:center;padding:0 110px;margin-top:34px}
.partner-badge{display:flex;align-items:center;gap:14px}
.badge-shape{width:74px;height:74px;background:#2c3266}
.badge-bar{width:140px;height:12px;background:#d3d7e2}
.badge-circle{border-radius:50%;background:#8b1e2b;width:64px;height:64px}

/* why */
.why{height:812px;background:linear-gradient(180deg,#ffffff 0%,#f3f6f9 60%,#eef2f7 100%)}
.why .section-title{padding-top:52px}
.why-media{position:absolute}
.media-surgeon{right:0;top:100px;width:360px;height:330px;
  background:linear-gradient(200deg,#5c8fc0 0%,#8fb4d6 35%,#d7e3ee 70%,#f3f6f9 100%);
  -webkit-mask-image:linear-gradient(90deg,transparent 0%,#000 35%);mask-image:linear-gradient(90deg,transparent 0%,#000 35%)}
.media-microscope{left:0;top:470px;width:560px;height:330px;
  background:linear-gradient(160deg,#dbe6f0 0%,#7ea6cc 40%,#4a7db0 65%,#c6d8e8 100%);
  -webkit-mask-image:linear-gradient(90deg,#000 55%,transparent 100%);mask-image:linear-gradient(90deg,#000 55%,transparent 100%)}
.feature{position:absolute;z-index:2}
.feature h3{font-size:30px;font-weight:300;color:var(--brand-light);margin-bottom:10px}
.feature p{font-size:14px;color:#333;margin-bottom:12px}
.feature ul{list-style:none;font-size:13px;color:#444;line-height:2}
.feature li::before{content:"•";color:var(--brand-light);margin-right:10px}
.feature-credible{left:182px;top:225px}
.feature-visual{left:597px;top:565px}

/* modules */
.modules{height:578px;background:var(--pale)}
.modules .section-title{padding-top:58px}
.module-grid{position:absolute;top:125px;left:78px;display:flex;gap:24px}
.module-card{width:331px;height:413px;background:var(--white);text-align:center}
.module-media{height:218px}
.module-card h4{font-size:19px;font-weight:400;margin:28px 0 10px}
.module-card p{font-size:13px;color:var(--muted);line-height:1.5;padding:0 40px;height:70px}
.module-card.featured{background:var(--brand)}
.module-card.featured h4,.module-card.featured p{color:var(--white)}

/* team */
.team{height:516px}
.team .section-title{padding-top:64px}
.team-grid{position:absolute;top:135px;left:78px;display:flex;gap:12px}
.team-card{width:254px;height:318px;border:1px solid var(--line);position:relative}
.team-media{height:252px}
.team-bar{position:absolute;left:0;right:0;bottom:0;height:66px;background:var(--brand);color:var(--white);padding:12px 14px}
.team-bar strong{display:block;font-weight:400;font-size:17px}
.team-bar span{font-size:11px;opacity:.75}
.team-bar svg{position:absolute;right:12px;top:15px}

/* testimonial */
.testimonial{height:406px;background:linear-gradient(90deg,#3c4a9e 0%,#4353a8 55%,#6c7bbf 100%)}
.testimonial-tone{position:absolute;right:0;top:0;width:520px;height:406px;background:linear-gradient(90deg,rgba(160,172,214,0),rgba(170,182,222,.45));}
.testimonial .section-title{color:var(--white);padding-top:58px}
.quote-photo{position:absolute;left:153px;top:135px;width:206px;height:206px;border:6px solid var(--white);background:linear-gradient(180deg,#cfd8e3 0%,#e2c6b0 45%,#c29e86 75%,#e9edf2 100%);z-index:2}
.quote-body{position:absolute;left:396px;top:128px;width:710px;color:var(--white);z-index:2}
.quote-mark{font-size:80px;line-height:.8;opacity:.35;font-family:Georgia,serif}
.quote-body p{font-size:15px;line-height:1.6;margin-top:14px;opacity:.92}
.quote-author{margin-top:18px;font-size:14px}
.quote-author span{opacity:.6;margin-left:10px;font-size:12px}

/* trial */
.trial{height:281px;text-align:center}
.trial .section-title{padding-top:64px}
.trial p{font-size:13px;color:#9aa0b0;margin:24px 0}

/* video */
.video{height:569px}
.video-media{position:absolute;inset:0;background:
  linear-gradient(180deg,rgba(20,30,50,.15) 0%,rgba(20,30,50,0) 30%,rgba(20,30,50,.25) 100%),
  linear-gradient(90deg,#e8eef3 0%,#c9b8aa 18%,#d9dfe6 34%,#8fa3b8 50%,#4b5f7a 68%,#2c3a52 85%,#1f2a3e 100%)}
.video-play{position:absolute;left:550px;top:234px}

/* charity */
.charity{height:228px;text-align:center}
.charity .section-title{padding-top:58px}
.charity p{width:780px;margin:24px auto 0;font-size:13px;line-height:1.6;color:#a0a5b2}

/* footer */
.site-footer{height:297px;background:var(--brand);color:var(--white);display:flex;padding:44px 78px 0}
.footer-col{font-size:12px}
.footer-brand{width:270px}
.footer-brand .brand-name{color:var(--white);font-size:26px}
.footer-brand .brand-sub{color:var(--white)}
.footer-brand p{margin-top:12px;line-height:1.6;opacity:.8}
.socials{display:flex;gap:10px;margin-top:20px;padding-left:50px}
.socials span{width:40px;height:40px;border-radius:50%;background:var(--white)}
.footer-links{width:262px}
.footer-col h5{font-size:20px;font-weight:400;margin-bottom:14px}
.footer-links ul{list-style:none;line-height:2.1;opacity:.85}
.footer-links li::before{content:"›";margin-right:8px}
.footer-news{width:260px}
.footer-news p{opacity:.85;line-height:1.6;margin-bottom:18px}
.footer-news .field{width:248px;height:42px;border:1px solid rgba(255,255,255,.4);background:rgba(255,255,255,.08);padding:12px;opacity:.8;margin-bottom:14px}
.footer-news .btn-sub{background:var(--white);color:var(--brand);font-size:15px;padding:11px 26px;display:inline-block}
.copyright{height:63px;background:#eef1f6;text-align:center;font-size:12px;color:#9aa0b0;line-height:63px}
.copyright strong{color:var(--brand);font-weight:500}
</style>
</head>
<body>

<header class="site-header">
  <a class="brand" href="#">
    <span class="brand-mark"></span>
    <span class="brand-name">Corvelle<span class="brand-sub">LEARNING HUB</span></span>
  </a>
  <nav class="main-nav">
    <a class="active" href="#">HOME</a>
    <a href="#">ABOUT</a>
    <a href="#">CHAPTERS</a>
    <a href="#">FAQ</a>
    <a href="#">CONTACT</a>
    <a class="login" href="#">LOGIN</a>
  </nav>
</header>

<section class="hero">
  <div class="hero-media" role="img" aria-label="Close-up photograph of a human eye with glowing circular scan lines">
    <div class="hero-tone"></div>
  </div>
  <div class="hero-copy">
    <h1>Learn Faster and Smarter</h1>
    <p>Corvelle Learning Hub helps undergraduates and healthcare professionals to learn or update their knowledge about the clinically relevant anatomy, ophthalmic examination techniques and common eye disorders of the human eye.</p>
    <a class="btn btn-dark" href="#">Undergraduates</a>
    <a class="btn btn-dark" href="#">Healthcare Professionals</a>
  </div>
</section>

<section class="partners">
  <h2 class="section-title">Trusted Across <span class="accent">The World</span></h2>
  <div class="partner-row">
    <div class="partner-badge"><span class="badge-shape" style="background:#c9a64a"></span><span class="badge-bar"></span></div>
    <div class="partner-badge"><span class="badge-shape"></span><span class="badge-bar"></span></div>
    <div class="partner-badge"><span class="badge-shape badge-circle"></span></div>
    <div class="partner-badge"><span class="badge-shape" style="background:#1f3f7a"></span><span class="badge-bar"></span></div>
  </div>
</section>

<section class="why">
  <h2 class="section-title">Why Corvelle <span class="accent">Training?</span></h2>
  <div class="why-media media-surgeon" role="img" aria-label="Photograph of a surgeon wearing magnifying loupes"></div>
  <div class="why-media media-microscope" role="img" aria-label="Photograph of a clinician at an operating microscope"></div>
  <div class="feature feature-credible">
    <h3>Credible</h3>
    <p>Written and illustrated by experienced Consultant Ophthalmologists.</p>
    <ul>
      <li>Designed and supported by experts</li>
      <li>Focused on constructive feedback, insights and action</li>
      <li>Continuously improved by 1000+ innovative companies</li>
    </ul>
  </div>
  <div class="feature feature-visual">
    <h3>Visual</h3>
    <p>Key concepts brought to life using stunning 3D animations</p>
    <ul>
      <li>Helps you build a comprehensive feedback strategy</li>
      <li>Gives your whole organization real-time, valuable insights</li>
      <li>Grows with your increasing needs</li>
    </ul>
  </div>
</section>

<section class="modules">
  <h2 class="section-title">Training <span class="accent">Modules</span></h2>
  <div class="module-grid">
    <article class="module-card">
      <div class="module-media" role="img" aria-label="Photograph of a trial frame used in eye testing" style="background:linear-gradient(180deg,#f4f1ee 0%,#e3d2c2 45%,#c9a889 70%,#f1ece7 100%)"></div>
      <h4>Core Principles</h4>
      <p>Diagnostic, deep dive and pulse surveys with powerful analytics and action planning.</p>
      <a class="btn btn-outline" href="#">Learn More</a>
    </article>
    <article class="module-card featured">
      <div class="module-media" role="img" aria-label="Photograph of a doctor examining an eye scan on screen" style="background:linear-gradient(120deg,#e9edf1 0%,#b9c9d8 35%,#5b6f8c 65%,#2b3448 100%)"></div>
      <h4>Ophthalmology in Practice</h4>
      <p>Automated employee surveys for each milestone: candidates, onboarding, exit and more.</p>
      <a class="btn btn-outline" href="#">Learn More</a>
    </article>
    <article class="module-card">
      <div class="module-media" role="img" aria-label="Photograph of smiling medical students in a group" style="background:linear-gradient(180deg,#b8d0a8 0%,#a9c0b8 35%,#7f9fc0 65%,#d6dde6 100%)"></div>
      <h4>AN Other</h4>
      <p>Action-oriented 180- and 360-feedback for managers, individuals and teams.</p>
      <a class="btn btn-outline" href="#">Learn More</a>
    </article>
  </div>
</section>

<section class="team">
  <h2 class="section-title">Meet the <span class="accent">Team</span></h2>
  <div class="team-grid">
    <article class="team-card">
      <div class="team-media" role="img" aria-label="Portrait photograph of a consultant in a white coat" style="background:linear-gradient(180deg,#eef1f4 0%,#d9c3b3 30%,#f2f4f7 55%,#c9d4e0 100%)"></div>
      <div class="team-bar"><strong>Alden Ruske</strong><span>Consultant Ophthalmologist</span>
        <svg width="36" height="36" viewBox="0 0 36 36"><circle cx="18" cy="18" r="16" fill="none" stroke="#fff" stroke-width="2"/><path d="M15 11l7 7-7 7" fill="none" stroke="#fff" stroke-width="2.5"/></svg></div>
    </article>
    <article class="team-card">
      <div class="team-media" role="img" aria-label="Portrait photograph of a consultant wearing glasses" style="background:linear-gradient(180deg,#6b4a38 0%,#d8b8a0 35%,#f3f3f5 60%,#cfd8e2 100%)"></div>
      <div class="team-bar"><strong>Marta Quillon</strong><span>Consultant Ophthalmologist</span>
        <svg width="36" height="36" viewBox="0 0 36 36"><circle cx="18" cy="18" r="16" fill="none" stroke="#fff" stroke-width="2"/><path d="M15 11l7 7-7 7" fill="none" stroke="#fff" stroke-width="2.5"/></svg></div>
    </article>
    <article class="team-card">
      <div class="team-media" role="img" aria-label="Portrait photograph of a doctor with stethoscope" style="background:linear-gradient(180deg,#eef2f6 0%,#dcc2ae 30%,#f4f6f8 55%,#aebfd2 100%)"></div>
      <div class="team-bar"><strong>Jonas Brevik</strong><span>CTO</span>
        <svg width="36" height="36" viewBox="0 0 36 36"><circle cx="18" cy="18" r="16" fill="none" stroke="#fff" stroke-width="2"/><path d="M15 11l7 7-7 7" fill="none" stroke="#fff" stroke-width="2.5"/></svg></div>
    </article>
    <article class="team-card">
      <div class="team-media" role="img" aria-label="Portrait photograph of a young doctor" style="background:linear-gradient(180deg,#e6ecf2 0%,#d6b9a2 30%,#f3f5f7 55%,#9fb2c8 100%)"></div>
      <div class="team-bar"><strong>Lorem ipsum text</strong><span>Lorem ipsum</span>
        <svg width="36" height="36" viewBox="0 0 36 36"><circle cx="18" cy="18" r="16" fill="none" stroke="#fff" stroke-width="2"/><path d="M15 11l7 7-7 7" fill="none" stroke="#fff" stroke-width="2.5"/></svg></div>
    </article>
  </div>
</section>

<section class="testimonial">
  <div class="testimonial-tone" role="img" aria-label="Faded photograph of clinicians in a training session"></div>
  <h2 class="section-title">Client Testimonial</h2>
  <div class="quote-photo" role="img" aria-label="Portrait photograph of the reviewing surgeon"></div>
  <div class="quote-body">
    <div class="quote-mark">“</div>
    <p>This is a unique website beautifully illustrated with 3D animations. It provides an excellent training guide for anyone wishing to learn basic ophthalmology and is also very useful for more senior ophthalmologists to use for their own teaching purposes. I have no hesitation in recommending this website very highly indeed.</p>
    <div class="quote-author">Mr Edwin Harrowgate FRCS FRCOphth <span>Westbury College School of Medicine</span></div>
  </div>
</section>

<section class="trial">
  <h2 class="section-title">Want to try Corvelle <span class="accent">Training for free?</span></h2>
  <p>No credit card details required it's completely free for 3 days.</p>
  <a class="btn btn-brand" href="#">Start Free Trial</a>
</section>

<section class="video">
  <div class="video-media" role="img" aria-label="Video still of a smiling doctor beside a slit lamp with a patient"></div>
  <svg class="video-play" width="100" height="100" viewBox="0 0 100 100"><circle cx="50" cy="50" r="48" fill="#2a2f3a" opacity=".85"/><path d="M40 30l30 20-30 20z" fill="#fff"/></svg>
</section>

<section class="charity">
  <h2 class="section-title">We give 10% <span class="accent">of our profits to charity</span></h2>
  <p>We believe it is important to give something back so from 2018 we will donate 10% to every subscription to a selected charity somewhere in the world which works to help prevent sight loss and treat eye diseases.</p>
</section>

<footer class="site-footer">
  <div class="footer-col footer-brand">
    <span class="brand-name">Corvelle<span class="brand-sub">LEARNING HUB</span></span>
    <p>Regularly reviewed and updated, this is a great place to help you better understand whether our course will be of value to you.</p>
    <div class="socials"><span></span><span></span><span></span></div>
  </div>
  <div class="footer-col footer-links">
    <h5>Company</h5>
    <ul><li>Home</li><li>About Us</li><li>Blog</li><li>Chapters</li><li>Contact us</li></ul>
  </div>
  <div class="footer-col footer-links">
    <h5>Policies</h5>
    <ul><li>Terms of use</li><li>Privacy and Cookies</li></ul>
  </div>
  <div class="footer-col footer-news">
    <h5>Newsletter</h5>
    <p>Subscribe to Our Newsletter to Get Latest Updates &amp; News.</p>
    <div class="field">Email</div>
    <span class="btn-sub">Subscribe</span>
  </div>
</footer>
<div class="copyright">© <strong>corvelle learning hub</strong> · 2018 · All Rights Reserved · Privacy · Sitemap</div>

</body>
</html>
```